Website redesign

Redesign the Website

http://www.lindmark-schoefer.de/

Task

- make 1 Layout for the Website
- Colors: white, yellow, brown
- Text: Take from Page - ore rather Use Latin - Lore Ipsum ...
- pimp design and overall look
- enhance overview for better orientation
- more freindly / sympatic overall look.
- Better integrate Mingleroo Button aso.
- send Layout as layered PSD

```html
<!DOCTYPE html>
<html lang="de">
<head>
<meta charset="utf-8">
<title>Lindmark Schöfer – Trauringe</title>
<link rel="stylesheet" href="https://fonts.googleapis.com/css2?family=Open+Sans:wght@400;600;700&display=swap">
<style>
:root{
  --brown:#5a2e14;
  --brown-dark:#4a240f;
  --yellow:#f2b705;
  --white:#ffffff;
  --text:#4a4a4a;
  --line:#d9d2cb;
  --tile:#f6f6f6;
  --gold-a:#e9cf86;
  --gold-b:#f7ecc9;
  --silver-a:#d7dbe0;
  --silver-b:#f1f2f4;
}
*{box-sizing:border-box;margin:0;padding:0}
html,body{width:1200px;height:2384px;overflow:hidden}
body{position:relative;background:var(--white);font-family:"Open Sans",Arial,sans-serif;color:var(--text)}
.topbar{position:absolute;left:0;top:0;width:1200px;height:28px;background:var(--brown);color:#f3e6d6;font-size:12px;display:flex;justify-content:center;align-items:center;gap:14px}
.topbar .sep{opacity:.6}
.header{position:absolute;left:0;top:28px;width:1200px;height:64px;display:flex;align-items:center;justify-content:space-between;padding:0 40px;border-bottom:1px solid var(--line)}
.logo{display:flex;align-items:center;gap:10px;font-size:22px;font-weight:700;color:var(--brown);letter-spacing:.5px}
.logo .dot{width:14px;height:14px;border-radius:50%;background:var(--yellow)}
.nav{display:flex;align-items:center;font-size:14px}
.nav a{color:var(--brown);text-decoration:none;padding:5px 10px;border-left:1px solid var(--line)}
.nav a:first-child{border-left:none}
.nav a.active{background:var(--yellow);color:var(--white)}
.hero{position:absolute;left:0;top:92px;width:1200px;height:556px;background:linear-gradient(180deg,#6fb0e6 0%,#bfe0f5 38%,#f6f7e8 52%,#c8d84a 62%,#8fb53a 80%,#5e8a2a 100%)}
.hero-box{position:absolute;left:340px;top:258px;width:520px;height:116px;background:rgba(90,90,90,.72);color:var(--white);text-align:center;padding-top:14px}
.hero-box h1{font-size:24px;font-weight:600}
.hero-box p{font-size:17px;line-height:24px}
.brand-divider{position:absolute;left:40px;top:744px;width:1120px;height:48px;display:flex;align-items:center;gap:24px}
.brand-divider .rule{flex:1;height:2px;background:var(--line)}
.brand-name{font-size:20px;font-weight:600;color:#555;letter-spacing:4px}
.edition{position:absolute;left:40px;width:1120px}
.edition-head{height:40px;border-bottom:3px solid var(--brown);position:relative}
.edition-label{position:absolute;left:0;top:0;height:40px;padding:0 20px;background:var(--yellow);color:var(--white);font-weight:700;font-size:17px;line-height:40px;letter-spacing:1px}
.ring-row{display:flex;justify-content:space-between;margin-top:40px}
.ring-tile{width:176px;height:176px;border:1px solid #ececec;background:var(--tile)}
.ring-tile.gold{background:linear-gradient(135deg,var(--gold-b) 0%,var(--gold-a) 100%)}
.ring-tile.silver{background:linear-gradient(135deg,var(--silver-b) 0%,var(--silver-a) 100%)}
.ring-tile.mixed{background:linear-gradient(135deg,var(--gold-a) 0%,var(--gold-b) 50%,var(--silver-a) 100%)}
.design-box{position:absolute;left:40px;top:1788px;width:360px;height:360px}
.design-box h2{height:52px;background:var(--brown);color:var(--white);font-size:18px;font-weight:600;line-height:52px;padding-left:22px}
.design-photo{height:308px;background:linear-gradient(135deg,var(--gold-b) 0%,var(--gold-a) 100%)}
.video{position:absolute;left:440px;top:1788px;width:720px;height:360px;background:linear-gradient(160deg,#3a2a22 0%,#8a6a55 45%,#c9a78b 70%,#2e2620 100%)}
.video-title{position:absolute;left:0;top:0;width:100%;height:36px;background:rgba(0,0,0,.55);color:#fff;font-size:14px;line-height:36px;padding-left:14px}
.video-bar{position:absolute;left:0;bottom:0;width:100%;height:30px;background:rgba(0,0,0,.7)}
.video-play{position:absolute;left:320px;top:150px}
.footer{position:absolute;left:0;top:2192px;width:1200px;height:192px;background:var(--yellow);padding:36px 40px 0}
.footer-cols{display:flex;gap:60px}
.footer ul{list-style:none;width:200px;font-size:13px;color:var(--brown)}
.footer li{line-height:26px;padding-left:16px;position:relative}
.footer li::before{content:"";position:absolute;left:0;top:10px;width:6px;height:6px;background:var(--brown)}
.footer-logo{position:absolute;right:40px;top:70px;display:flex;align-items:center;gap:10px;font-size:24px;font-weight:700;color:var(--brown)}
.footer-logo .dot{width:14px;height:14px;border-radius:50%;background:var(--white)}
</style>
</head>
<body>
<div class="topbar">
  <span>Lindmark Schöfer GmbH</span><span class="sep">|</span>
  <span>Erlenweg 7</span><span class="sep">|</span>
  <span>40999 Brunnhagen</span><span class="sep">|</span>
  <span>Tel: 0555-010230</span><span class="sep">|</span>
  <span>Fax: 0555-010231</span><span class="sep">|</span>
  <span>info@lindmark-schoefer.de</span>
</div>

<header class="header">
  <div class="logo"><span class="dot"></span>LINDMARK SCHÖFER.DE</div>
  <nav class="nav">
    <a href="#">Trauringe</a><a href="#">Solitairringe</a><a href="#" class="active">Partnerringe</a><a href="#">Brautschmuck</a><a href="#">Informationen</a><a href="#">Kontakt</a>
  </nav>
</header>

<section class="hero" role="img" aria-label="Feldweg durch blühende Rapsfelder unter blauem Himmel mit Trauringen">
  <div class="hero-box">
    <h1>Ihr Weg zum Glück...</h1>
    <p>...führt unser Weg: Juwelier<br>am Erlenweg 7 in 40999 Brunnhagen</p>
  </div>
</section>

<div class="brand-divider">
  <span class="rule"></span><span class="brand-name">VELLMAR</span><span class="rule"></span>
</div>

<section class="edition" style="top:832px">
  <div class="edition-head"><span class="edition-label">EDITION - I</span></div>
  <div class="ring-row">
    <div class="ring-tile mixed" role="img" aria-label="Produktfoto: Trauringpaar Gold und Weißgold"></div>
    <div class="ring-tile silver" role="img" aria-label="Produktfoto: Trauringpaar Weißgold"></div>
    <div class="ring-tile silver" role="img" aria-label="Produktfoto: Trauringpaar Weißgold mit Stein"></div>
    <div class="ring-tile gold" role="img" aria-label="Produktfoto: Trauringpaar Gelbgold mit Stein"></div>
    <div class="ring-tile gold" role="img" aria-label="Produktfoto: Trauringpaar Gelbgold"></div>
  </div>
</section>

<section class="edition" style="top:1132px">
  <div class="edition-head"><span class="edition-label">EDITION - I</span></div>
  <div class="ring-row">
    <div class="ring-tile mixed" role="img" aria-label="Produktfoto: Trauringpaar Gold und Weißgold"></div>
    <div class="ring-tile silver" role="img" aria-label="Produktfoto: Trauringpaar Weißgold"></div>
    <div class="ring-tile silver" role="img" aria-label="Produktfoto: Trauringpaar Weißgold mit Stein"></div>
    <div class="ring-tile gold" role="img" aria-label="Produktfoto: Trauringpaar Gelbgold mit Stein"></div>
    <div class="ring-tile gold" role="img" aria-label="Produktfoto: Trauringpaar Gelbgold"></div>
  </div>
</section>

<section class="edition" style="top:1432px">
  <div class="edition-head"><span class="edition-label">EDITION - I</span></div>
  <div class="ring-row">
    <div class="ring-tile mixed" role="img" aria-label="Produktfoto: Trauringpaar Gold und Weißgold"></div>
    <div class="ring-tile silver" role="img" aria-label="Produktfoto: Trauringpaar Weißgold"></div>
    <div class="ring-tile silver" role="img" aria-label="Produktfoto: Trauringpaar Weißgold mit Stein"></div>
    <div class="ring-tile gold" role="img" aria-label="Produktfoto: Trauringpaar Gelbgold mit Stein"></div>
    <div class="ring-tile gold" role="img" aria-label="Produktfoto: Trauringpaar Gelbgold"></div>
  </div>
</section>

<aside class="design-box">
  <h2>Trauring selbst gestalten</h2>
  <div class="design-photo" role="img" aria-label="Produktfoto: zwei goldene Trauringe"></div>
</aside>

<div class="video" role="img" aria-label="Video: Goldschmied bei der Arbeit an einem Ring">
  <div class="video-title">Der Ring vom Goldschmied: Neue Kollektion</div>
  <svg class="video-play" width="80" height="56" viewBox="0 0 80 56"><rect width="80" height="56" rx="12" fill="#222" fill-opacity=".85"/><path d="M32 16 L54 28 L32 40 Z" fill="#fff"/></svg>
  <div class="video-bar"></div>
</div>

<footer class="footer">
  <div class="footer-cols">
    <ul><li>Lindmark Schöfer</li><li>Edition I</li><li>Edition II</li><li>Edition III</li><li>Kollektion</li></ul>
    <ul><li>Neue Kollektion</li><li>Partnerringe</li><li>Über uns</li><li>Kontakt</li></ul>
    <ul><li>Eigene Gestaltung</li><li>Ringgrößen Tabelle</li><li>Werkstatt</li><li>Impressum</li></ul>
  </div>
  <div class="footer-logo"><span class="dot"></span>LINDMARK SCHÖFER.DE</div>
</footer>
</body>
</html>
```